Tobias Grünwald and Co stationary design

Name of business:
Tobias Grünwald and Co

Can be written as:
Tobias Grünwald and Co
Tobias Grünwald & Co
tobias grünwald & co

If broken into letters:
TG&Co
tg&co

We are a Railway Safety Training Company
Our focus is on rail safety, Rail Management, Safety Management, Train Control Training, Accident Investigation.

.
Updates

Project Deadline Extended Reason: The original date was set to commence as soon as the logo contest finished. Quillset hub started the project as soon as it was paid. Added Thursday, May 12, 2016

Target Market(s)

Professionals, CEO's and Managing Directors

Industry/Entity Type

Management Consulting

Font styles to use
Sans Serif

Requirements
Must have
• Professional, Sharp, Creative and modern
• Please note that this is for stationary concept which must include
• - business card
• - letterhead
• - envelope
• - with compliments slip
• - document cover (like book or folder cover)
• - dividers for folders....
• These must all have a common theme or style
Nice to have
• Keep if fresh
Should not have
• Please don't sent just fonts.... Must be creative

```html
<!DOCTYPE html>
<html lang="en">
<head>
<meta charset="utf-8">
<title>Tobias Grünwald &amp; Co — Stationery</title>
<link rel="stylesheet" href="https://fonts.googleapis.com/css2?family=Open+Sans:wght@400;600;700&display=swap">
<style>
  :root {
    --navy: #13478a;
    --navy-dark: #0f3c78;
    --orange: #f4a21e;
    --white: #ffffff;
    --stage: #a9a9a9;
    --ink: #1b2430;
    --shadow: 4px 6px 10px rgba(0,0,0,.28);
  }
  * { box-sizing: border-box; margin: 0; padding: 0; }
  html, body { width: 1200px; height: 1200px; overflow: hidden; }
  body { background: var(--stage); font-family: "Open Sans", sans-serif; color: var(--ink); position: relative; }
  .sheet { position: absolute; background: var(--white); box-shadow: var(--shadow); overflow: hidden; }
  .sheet--navy { background: var(--navy); color: var(--white); }

  .brand { display: flex; align-items: center; gap: 6px; font-weight: 700; color: var(--navy); white-space: nowrap; }
  .brand__dot { border-radius: 50%; background: var(--orange); flex: none; }
  .brand--light { color: var(--white); }

  .icon { width: 7px; height: 7px; fill: currentColor; flex: none; }
  .contact { display: flex; flex-direction: column; gap: 2px; font-size: 8px; line-height: 1.25; }
  .contact__row { display: flex; align-items: center; gap: 6px; }
  .contact__gap { height: 4px; }

  .person__name { font-size: 9px; font-weight: 700; }
  .person__role { font-size: 7.5px; }

  /* business cards */
  .card-front { left: 52px; top: 44px; width: 266px; height: 160px; padding: 18px 16px; }
  .card-front .person__name { color: var(--orange); }
  .card-front .contact { margin-top: 34px; }
  .card-front .brand { position: absolute; right: 12px; bottom: 20px; font-size: 9px; }
  .card-back { left: 346px; top: 44px; width: 266px; height: 160px; display: flex; align-items: center; justify-content: center; }
  .card-back .brand { font-size: 14px; flex-direction: column; gap: 10px; }

  .card-white { left: 52px; top: 239px; width: 268px; height: 162px; padding: 18px 16px; }
  .card-white .person__name { color: var(--navy); }
  .card-white .brand { position: absolute; left: 16px; top: 88px; font-size: 9px; flex-direction: column; gap: 8px; }
  .card-white .contact { position: absolute; left: 146px; top: 74px; padding-left: 10px; border-left: 1px solid var(--navy); }
  .card-white .contact__addr { color: var(--navy); }

  .card-pattern { left: 345px; top: 239px; width: 268px; height: 162px; }
  .card-pattern__field { position: absolute; inset: 0; background: linear-gradient(135deg, #1a4e92, #2a5c9d 50%, #1a4e92); }
  .card-pattern .brand { position: absolute; right: 20px; bottom: 40px; font-size: 7px; }

  /* compliments slip */
  .slip { left: 677px; top: 33px; width: 334px; height: 166px; }
  .slip__title { position: absolute; right: 16px; top: 13px; font-size: 10.5px; color: var(--navy); }
  .slip__foot { position: absolute; left: 14px; bottom: 12px; display: flex; align-items: center; gap: 6px; }
  .slip__foot .brand { font-size: 4.5px; }
  .tiny { font-size: 4.2px; line-height: 1.3; color: var(--navy); padding-left: 5px; border-left: .6px solid var(--navy); gap: 0; }

  /* envelopes */
  .env-front { left: 677px; top: 226px; width: 398px; height: 198px; padding: 12px 13px; }
  .env-front .brand { font-size: 5px; flex-direction: column; align-items: flex-start; gap: 3px; }
  .env-front__addr { font-size: 4.2px; line-height: 1.3; color: var(--navy); margin-top: 3px; }
  .env-back { left: 677px; top: 445px; width: 398px; height: 198px; }
  .env-back__flap { position: absolute; inset: 0; width: 100%; height: 70px; }
  .env-back .brand { position: absolute; left: 50%; top: 22px; transform: translateX(-50%); font-size: 6px; }

  /* letterhead */
  .letterhead { left: 49px; top: 484px; width: 458px; height: 648px; }
  .letterhead__head { position: absolute; left: 0; right: 0; top: 26px; display: flex; justify-content: center; }
  .letterhead__head .brand { font-size: 9px; flex-direction: column; gap: 8px; }
  .letterhead__foot { position: absolute; left: 0; right: 0; bottom: 18px; text-align: center; font-size: 6px; color: var(--navy); }
  .letterhead__line { display: flex; justify-content: center; gap: 14px; color: var(--ink); margin-bottom: 4px; }
  .letterhead__line span { display: flex; align-items: center; gap: 4px; }
  .letterhead__bar { position: absolute; left: 0; right: 0; bottom: 0; height: 8px; background: var(--navy); }

  /* folder */
  .folder-back { left: 580px; top: 690px; width: 270px; height: 420px; background: linear-gradient(90deg, #f2f2f2, #ffffff); }
  .folder-back__mark { position: absolute; left: 45px; top: 140px; width: 160px; height: 160px; border-radius: 50%; border: 14px solid rgba(19,71,138,.07); }
  .folder-back__foot { position: absolute; left: 12px; bottom: 40px; display: flex; align-items: center; gap: 6px; }
  .folder-back__foot .brand { font-size: 4px; }
  .folder-front { left: 850px; top: 690px; width: 270px; height: 420px; }
  .folder-front__head { position: absolute; left: 0; right: 0; top: 36px; display: flex; justify-content: center; }
  .folder-front__head .brand { font-size: 9px; flex-direction: column; gap: 8px; }
  .folder-front__visual { position: absolute; left: 0; top: 110px; width: 270px; height: 170px; }
  .folder-front__headline { position: absolute; left: 0; right: 0; top: 316px; text-align: center; font-size: 16px; line-height: 1.25; color: var(--navy); }
  .folder-front__body { position: absolute; left: 22px; right: 22px; top: 366px; font-size: 7px; line-height: 1.35; color: var(--ink); }
</style>
</head>
<body>

<svg width="0" height="0" style="position:absolute" aria-hidden="true">
  <defs>
    <symbol id="i-phone" viewBox="0 0 10 10"><path d="M2 0h6v10H2z M3 1v7h4V1z"/></symbol>
    <symbol id="i-call" viewBox="0 0 10 10"><path d="M2 1c1-1 2 0 2.5 1.5L3.5 4c.6 1.3 1.3 2 2.5 2.5L7.5 5.5C9 6 10 7 9 8 7 10 0 4 2 1z"/></symbol>
    <symbol id="i-mail" viewBox="0 0 10 10"><path d="M0 2h10v7H0z M1 3l4 3 4-3z" fill-rule="evenodd"/></symbol>
    <symbol id="i-web" viewBox="0 0 10 10"><path d="M5 0a5 5 0 1 0 0 10A5 5 0 0 0 5 0zm0 1.2a3.8 3.8 0 1 1 0 7.6A3.8 3.8 0 0 1 5 1.2zM1 4.5h8v1H1z" fill-rule="evenodd"/></symbol>
  </defs>
</svg>

<!-- business card, navy front -->
<section class="sheet sheet--navy card-front">
  <p class="person__name">Maren Holt</p>
  <p class="person__role">Director</p>
  <div class="contact">
    <span class="contact__row"><svg class="icon" style="color:var(--orange)"><use href="#i-phone"/></svg>+1 555 014 2290</span>
    <span class="contact__row"><svg class="icon" style="color:var(--orange)"><use href="#i-call"/></svg>+1 555 270 0184</span>
    <span class="contact__row"><svg class="icon" style="color:var(--orange)"><use href="#i-mail"/></svg>info@tgco-rail.com.au</span>
    <span class="contact__row"><svg class="icon" style="color:var(--orange)"><use href="#i-web"/></svg>www.tgco-rail.com.au</span>
    <span class="contact__gap"></span>
    <span>48 Harbour Line Rd, Suite 12</span>
    <span>Eastwick, City 40210</span>
  </div>
  <div class="brand brand--light"><span class="brand__dot" style="width:10px;height:10px"></span>TG&amp;Co</div>
</section>

<!-- business card, navy back -->
<section class="sheet sheet--navy card-back">
  <div class="brand brand--light"><span class="brand__dot" style="width:22px;height:22px"></span>Tobias Grünwald &amp; Co</div>
</section>

<!-- business card, white front -->
<section class="sheet card-white">
  <p class="person__name">Maren Holt</p>
  <p class="person__role">Director</p>
  <div class="brand"><span class="brand__dot" style="width:20px;height:20px"></span>Tobias Grünwald &amp; Co</div>
  <div class="contact">
    <span class="contact__row"><svg class="icon" style="color:var(--navy)"><use href="#i-phone"/></svg>+61 555 014 2290</span>
    <span class="contact__row"><svg class="icon" style="color:var(--navy)"><use href="#i-call"/></svg>+61 555 270 0184</span>
    <span class="contact__row"><svg class="icon" style="color:var(--navy)"><use href="#i-mail"/></svg>info@tgco-rail.com.au</span>
    <span class="contact__row"><svg class="icon" style="color:var(--navy)"><use href="#i-web"/></svg>www.tgco-rail.com.au</span>
    <span class="contact__addr">48 Harbour Line Rd, Suite 12</span>
    <span class="contact__addr">Eastwick, CA 40210</span>
  </div>
</section>

<!-- business card, pattern back -->
<section class="sheet sheet--navy card-pattern">
  <div class="card-pattern__field" role="img" aria-label="Repeating brand pattern in muted blue tones"></div>
  <div class="brand brand--light"><span class="brand__dot" style="width:9px;height:9px"></span>Tobias Grünwald &amp; Co</div>
</section>

<!-- with compliments slip -->
<section class="sheet slip">
  <p class="slip__title">With Compliments</p>
  <div class="slip__foot">
    <div class="brand"><span class="brand__dot" style="width:7px;height:7px"></span>Tobias Grünwald &amp; Co</div>
    <div class="contact tiny">
      <span>+61 555 270 0184</span>
      <span>info@tgco-rail.com.au</span>
      <span>www.tgco-rail.com.au</span>
      <span>48 Harbour Line Rd, Suite 12</span>
      <span>Eastwick, CA 40210</span>
    </div>
  </div>
</section>

<!-- envelope, front -->
<section class="sheet env-front">
  <div class="brand"><span class="brand__dot" style="width:12px;height:12px"></span>Tobias Grünwald &amp; Co</div>
  <p class="env-front__addr">48 Harbour Line Rd, Suite 12<br>Eastwick, City 40210</p>
</section>

<!-- envelope, back -->
<section class="sheet env-back">
  <svg class="env-back__flap" viewBox="0 0 398 70" preserveAspectRatio="none" aria-hidden="true">
    <path d="M1 0 C10 30 20 58 40 58 H358 C378 58 388 30 397 0" fill="none" stroke="#9a9a9a" stroke-width="1"/>
  </svg>
  <div class="brand"><span class="brand__dot" style="width:10px;height:10px"></span>TG&amp;Co</div>
</section>

<!-- letterhead -->
<section class="sheet letterhead">
  <div class="letterhead__head">
    <div class="brand"><span class="brand__dot" style="width:26px;height:26px"></span>Tobias Grünwald &amp; Co</div>
  </div>
  <div class="letterhead__foot">
    <p class="letterhead__line">
      <span><svg class="icon" style="color:var(--navy);width:6px;height:6px"><use href="#i-call"/></svg>+1 555 270 0184</span>
      <span><svg class="icon" style="color:var(--navy);width:6px;height:6px"><use href="#i-mail"/></svg>info@tgco-rail.com.au</span>
      <span><svg class="icon" style="color:var(--navy);width:6px;height:6px"><use href="#i-web"/></svg>www.tgco-rail.com.au</span>
    </p>
    <p>48 Harbour Line Rd, Suite 12, Eastwick, City 40210</p>
  </div>
  <div class="letterhead__bar"></div>
</section>

<!-- document folder, back panel -->
<section class="sheet folder-back">
  <div class="folder-back__mark" aria-hidden="true"></div>
  <div class="folder-back__foot">
    <div class="brand"><span class="brand__dot" style="width:7px;height:7px"></span>TG&amp;Co</div>
    <div class="contact tiny">
      <span>+61 555 270 0184</span>
      <span>info@tgco-rail.com.au</span>
      <span>48 Harbour Line Rd</span>
      <span>Eastwick, CA 40210</span>
    </div>
  </div>
</section>

<!-- document folder, front panel -->
<section class="sheet folder-front">
  <div class="folder-front__head">
    <div class="brand"><span class="brand__dot" style="width:26px;height:26px"></span>Tobias Grünwald &amp; Co</div>
  </div>
  <svg class="folder-front__visual" viewBox="0 0 270 170" aria-hidden="true">
    <defs>
      <linearGradient id="photo-tones" x1="0" y1="0" x2="1" y2="1">
        <stop offset="0" stop-color="#c9d3de"/>
        <stop offset="1" stop-color="#7f8a97"/>
      </linearGradient>
    </defs>
    <path d="M0 0 C70 10 140 40 270 140 V170 H0 Z" fill="#ffffff"/>
    <path d="M0 0 C80 8 160 50 220 90 L160 160 L70 110 L0 150 Z" fill="url(#photo-tones)"/>
    <path d="M170 60 C200 45 235 38 270 36 V60 C240 62 210 66 190 72 Z" fill="var(--orange)"/>
    <path d="M0 0 C80 8 160 50 220 90" fill="none" stroke="var(--navy)" stroke-width="1"/>
    <path d="M70 110 L160 160 L220 90" fill="none" stroke="var(--navy)" stroke-width="1"/>
    <path d="M220 90 L270 140" fill="none" stroke="var(--navy)" stroke-width="1"/>
  </svg>
  <div role="img" aria-label="Photographs of business professionals at work" style="position:absolute;left:0;top:110px;width:220px;height:160px"></div>
  <h2 class="folder-front__headline" style="font-weight:400">YOUR MAIN<br>HEADLINE HERE</h2>
  <p class="folder-front__body">Lorem Ipsum is simply dummy text of the printing and typesetting industry. Lorem Ipsum has been the industry's standard dummy</p>
</section>

</body>
</html>
```